Business Card Design

I am an Event and Wedding Planner in need of an eye catching business card featuring my logo (attached), my contact details, and my company tagline (Making each one of your gatherings radiant...) I would like the tagline in font similar the logo's font.
Updates
I have just noticed that my logo has a misspelling so for the final design, I will be uploading a corrected logo as soon as I have it.
My apologies.
Reason: Waiting on a corrected logo...Occasions is misspelled and it should say Weddings not Wedding
The logo has been corrected so now Occasions is spelled correctly and it says Weddings instead of Wedding. Please use Edwardian Script ITC as the font for the tagline so it will match the logo. Thank you for your patience.
Target Market(s)
Engaged couples and people hosting milestone celebrations. 25-50 years old, predominately female
Industry/Entity Type
Business
Contact Information for Business Card
Delphine Marsh, Event Manager / Owner, Mobile: 0491 836 254, Email: delphine@radiantgatheringsco.com.au, www.radiantgatheringsco.com.au, Making each one of your gatherings radiant...

```html
<!DOCTYPE html>
<html lang="en">
<head>
<meta charset="utf-8">
<title>Radiant Gatherings Co. – Business Card</title>
<link href="https://fonts.googleapis.com/css2?family=Great+Vibes&family=Tinos&family=Open+Sans:wght@400&display=swap" rel="stylesheet">
<style>
  :root {
    --backdrop: #ebe6de;
    --card-light: #f7f7f7;
    --card-mid: #dcdcdc;
    --crimson: #c0213a;
    --crimson-dark: #9d1a2e;
    --charcoal: #3a3a3a;
    --slate: #6b6b6b;
    --white: #ffffff;
  }
  * { margin: 0; padding: 0; box-sizing: border-box; }
  html, body { width: 1200px; height: 1000px; overflow: hidden; }
  body {
    background: var(--backdrop);
    position: relative;
    font-family: "Open Sans", sans-serif;
  }
  .card {
    position: absolute;
    top: 132px;
    width: 420px;
    height: 735px;
    overflow: hidden;
    box-shadow: 0 10px 30px rgba(0,0,0,0.18);
    background: linear-gradient(160deg, var(--white) 0%, var(--card-light) 45%, var(--card-mid) 100%);
  }
  .card--front { left: 150px; }
  .card--back { left: 630px; }

  /* Front */
  .brand {
    position: absolute;
    top: 170px; left: 0; right: 0;
    text-align: center;
  }
  .brand__name {
    font-family: "Great Vibes", cursive;
    font-size: 58px;
    line-height: 1.05;
    color: var(--charcoal);
  }
  .brand__rule {
    width: 300px; height: 1px;
    margin: 22px auto 0;
    background: var(--slate);
  }
  .brand__dot {
    display: block;
    width: 14px; height: 14px;
    margin: 18px auto 0;
    border-radius: 50%;
    background: var(--crimson);
  }
  .front-base {
    position: absolute;
    left: 0; bottom: 0;
    width: 420px; height: 260px;
  }
  .tagline {
    position: absolute;
    left: 40px; right: 30px;
    bottom: 130px;
    font-family: "Great Vibes", cursive;
    font-size: 30px;
    line-height: 1.15;
    color: var(--crimson);
    text-align: right;
  }

  /* Back */
  .person {
    position: absolute;
    top: 300px; left: 40px;
    font-family: "Tinos", serif;
  }
  .person__name {
    font-size: 34px;
    color: var(--crimson);
  }
  .person__role {
    margin-top: 14px;
    font-size: 20px;
    color: var(--slate);
  }
  .back-base {
    position: absolute;
    left: 0; bottom: 0;
    width: 420px; height: 320px;
  }
  .contacts {
    position: absolute;
    left: 40px; bottom: 56px;
    list-style: none;
    color: var(--white);
    font-size: 14.5px;
  }
  .contacts li {
    display: flex;
    align-items: center;
    gap: 12px;
    margin-top: 20px;
  }
  .contacts svg { flex: none; }
</style>
</head>
<body>

  <section class="card card--front" aria-label="Business card front">
    <div class="brand">
      <div class="brand__name">Radiant<br>Gatherings Co.</div>
      <div class="brand__rule"></div>
      <span class="brand__dot"></span>
    </div>
    <svg class="front-base" viewBox="0 0 420 260" aria-hidden="true">
      <path d="M0 20 L60 20 L78 46 L420 46 L420 260 L0 260 Z" fill="var(--crimson)"/>
      <path d="M0 60 L420 60 L420 260 L0 260 Z" fill="var(--crimson-dark)" opacity="0.25"/>
      <path d="M0 42 L420 42 L420 160 L0 200 Z" fill="var(--white)"/>
      <path d="M30 0 L110 0 L140 42 L60 42 Z" fill="#e6e6e6"/>
      <path d="M60 42 L140 42 L95 60 Z" fill="#bdbdbd"/>
    </svg>
    <p class="tagline">Making each one of your<br>gatherings radiant...</p>
  </section>

  <section class="card card--back" aria-label="Business card back">
    <div class="person">
      <div class="person__name">Delphine Marsh</div>
      <div class="person__role">Event Manager / Owner</div>
    </div>
    <svg class="back-base" viewBox="0 0 420 320" aria-hidden="true">
      <path d="M0 0 L420 0 L420 320 L0 320 Z" fill="var(--crimson)"/>
      <path d="M0 0 L420 0 L420 40 L0 70 Z" fill="var(--crimson-dark)" opacity="0.35"/>
    </svg>
    <ul class="contacts">
      <li>
        <svg width="20" height="20" viewBox="0 0 20 20" aria-label="Phone"><circle cx="10" cy="10" r="10" fill="var(--white)"/><path d="M7 5 L9 5 L10 8 L8.6 9 Q9.6 11 11 11.4 L12 10 L15 11 L15 13 Q15 15 13 15 Q6 14 5 7 Q5 5 7 5 Z" fill="var(--crimson)"/></svg>
        <span>0491 836 254</span>
      </li>
      <li>
        <svg width="20" height="20" viewBox="0 0 20 20" aria-label="Email"><circle cx="10" cy="10" r="10" fill="var(--white)"/><rect x="5" y="6.5" width="10" height="7" fill="none" stroke="var(--crimson)" stroke-width="1.3"/><path d="M5 6.5 L10 10.5 L15 6.5" fill="none" stroke="var(--crimson)" stroke-width="1.3"/></svg>
        <span>delphine@radiantgatheringsco.com.au</span>
      </li>
      <li>
        <svg width="20" height="20" viewBox="0 0 20 20" aria-label="Website"><circle cx="10" cy="10" r="10" fill="var(--white)"/><circle cx="10" cy="10" r="5.5" fill="none" stroke="var(--crimson)" stroke-width="1.2"/><ellipse cx="10" cy="10" rx="2.3" ry="5.5" fill="none" stroke="var(--crimson)" stroke-width="1.1"/><path d="M4.5 10 H15.5" stroke="var(--crimson)" stroke-width="1.1"/></svg>
        <span>www.radiantgatheringsco.com.au</span>
      </li>
    </ul>
  </section>

</body>
</html>
```